Nonna's Vellato

I am looking to design a label to be used on a glass jar for packaging a very special spice that has been used in our family for generations. The spice is excellent on meats, burgers, poultry, fish, and more.

The name of the spice is "Nonna's Famous Vellato"

Design should be traditional, with an Italian feel.

Total circumference of the jar is 10"
Height of jar is 4"

Some of the glass should not be covered to reveal color of spice inside.

Target Market(s)

Female 25-75

```html
<!DOCTYPE html>
<html lang="en">
<head>
<meta charset="utf-8">
<title>Nonna's Famous Vellato – Jar Label</title>
<link rel="stylesheet" href="https://fonts.googleapis.com/css2?family=Playfair+Display:wght@700&family=Italianno&display=swap">
<style>
  :root {
    --page: #ffffff;
    --lid: #262626;
    --lid-shine: #4a4a4a;
    --neck: #f2f2f2;
    --neck-line: #b8b8b8;
    --glass-edge: #9a9a9a;
    --spice-green: #7d8f5e;
    --spice-light: #b7c0a0;
    --spice-dark: #4f5a3a;
    --band-green: #0b8a3e;
    --band-green-dark: #05612a;
    --gold: #d9b46a;
    --label-red: #c8201f;
    --label-red-dark: #9e1515;
    --burst: #ee5a22;
    --type-white: #ffffff;
    --dimension: #d6d6d6;
    --dimension-text: #c4c4c4;
  }
  html, body {
    margin: 0;
    padding: 0;
    width: 1200px;
    height: 1000px;
    overflow: hidden;
    background: var(--page);
  }
  .canvas { display: block; width: 1200px; height: 1000px; }
  .product-name {
    font-family: "Playfair Display", serif;
    font-weight: 700;
    font-size: 50px;
    letter-spacing: 1px;
    fill: var(--type-white);
  }
  .dimension-line { stroke: var(--dimension); stroke-width: 1; }
  .dimension-text {
    font-family: "Italianno", cursive;
    font-size: 40px;
    fill: var(--dimension-text);
  }
</style>
</head>
<body>
<svg class="canvas" viewBox="0 0 1200 1000" xmlns="http://www.w3.org/2000/svg">
  <defs>
    <linearGradient id="lid-gradient" x1="0" y1="0" x2="0" y2="1">
      <stop offset="0" stop-color="var(--lid-shine)"/>
      <stop offset="0.35" stop-color="var(--lid)"/>
      <stop offset="1" stop-color="#111"/>
    </linearGradient>
    <linearGradient id="neck-gradient" x1="0" y1="0" x2="1" y2="0">
      <stop offset="0" stop-color="#dcdcdc"/>
      <stop offset="0.5" stop-color="var(--neck)"/>
      <stop offset="1" stop-color="#d0d0d0"/>
    </linearGradient>
    <radialGradient id="spice-gradient" cx="0.5" cy="0.5" r="0.7">
      <stop offset="0" stop-color="var(--spice-green)"/>
      <stop offset="0.7" stop-color="var(--spice-dark)"/>
      <stop offset="1" stop-color="var(--spice-light)"/>
    </radialGradient>
    <linearGradient id="band-gradient" x1="0" y1="0" x2="0" y2="1">
      <stop offset="0" stop-color="var(--band-green)"/>
      <stop offset="1" stop-color="var(--band-green-dark)"/>
    </linearGradient>
    <linearGradient id="red-gradient" x1="0" y1="0" x2="1" y2="0">
      <stop offset="0" stop-color="var(--label-red-dark)"/>
      <stop offset="0.5" stop-color="var(--label-red)"/>
      <stop offset="1" stop-color="var(--label-red-dark)"/>
    </linearGradient>
    <radialGradient id="burst-gradient" cx="522" cy="560" r="240" gradientUnits="userSpaceOnUse">
      <stop offset="0" stop-color="var(--burst)" stop-opacity="1"/>
      <stop offset="0.55" stop-color="var(--burst)" stop-opacity="0.75"/>
      <stop offset="1" stop-color="var(--burst)" stop-opacity="0"/>
    </radialGradient>
    <clipPath id="jar-body-clip">
      <rect x="297" y="250" width="452" height="448" rx="46"/>
    </clipPath>
  </defs>

  <!-- Jar lid and neck -->
  <g class="jar-top">
    <rect class="jar-neck" x="378" y="212" width="297" height="40" fill="url(#neck-gradient)" stroke="var(--neck-line)" stroke-width="1"/>
    <line x1="380" y1="228" x2="673" y2="228" stroke="var(--neck-line)" stroke-width="1"/>
    <rect class="jar-lid" x="352" y="168" width="341" height="47" rx="9" fill="url(#lid-gradient)"/>
  </g>

  <!-- Jar body -->
  <g class="jar-body" clip-path="url(#jar-body-clip)">
    <rect class="spice-contents" x="297" y="250" width="452" height="448" fill="url(#spice-gradient)"
          role="img" aria-label="Dried green herb and spice blend visible through the glass"/>

    <g class="label-band">
      <rect x="297" y="362" width="452" height="16" fill="url(#band-gradient)"/>
      <rect x="297" y="378" width="452" height="3" fill="var(--gold)"/>
      <rect x="297" y="381" width="452" height="191" fill="url(#red-gradient)"/>
      <rect x="297" y="381" width="452" height="191" fill="url(#burst-gradient)"
            role="img" aria-label="Orange sunburst rays rising behind the product name"/>
      <rect x="297" y="572" width="452" height="3" fill="var(--gold)"/>
      <rect x="297" y="575" width="452" height="16" fill="url(#band-gradient)"/>

      <text class="product-name" x="523" y="0" text-anchor="middle">
        <tspan x="523" y="462">Nonna's Famous</tspan>
        <tspan x="523" y="526">Vellato</tspan>
      </text>
    </g>
  </g>
  <rect class="jar-outline" x="297" y="250" width="452" height="448" rx="46" fill="none" stroke="var(--glass-edge)" stroke-width="1.5"/>

  <!-- Height dimension -->
  <g class="dimension dimension-height">
    <line class="dimension-line" x1="893" y1="145" x2="893" y2="740"/>
    <line class="dimension-line" x1="790" y1="168" x2="1000" y2="168"/>
    <line class="dimension-line" x1="790" y1="698" x2="1000" y2="698"/>
    <text class="dimension-text" x="0" y="0" text-anchor="middle" transform="translate(892 442) rotate(-90)">100 mm</text>
  </g>

  <!-- Width dimension -->
  <g class="dimension dimension-width">
    <line class="dimension-line" x1="278" y1="800" x2="818" y2="800"/>
    <line class="dimension-line" x1="297" y1="737" x2="297" y2="830"/>
    <line class="dimension-line" x1="749" y1="737" x2="749" y2="830"/>
    <text class="dimension-text" x="530" y="795" text-anchor="middle">90 mm</text>
  </g>
</svg>
</body>
</html>
```